Stylish business cards for KX7

To create an appealing and professional business card design for a WOMEN Owned Construction Supply Company.
2 sided card. Incorporate brand elements, curvy, colorful, sleek and bright. No solid white background. attached samples of styles added shapes/ribbons. Want something with that WOW that looks awesome, factor. It is a new logo, so feel free to mess with logo colors in the blue and teal factors that can look good with both dark and light background. If you want to try a watermark with just the KX7, without the "Supply" that might look cool to.

Industry/Entity Type

Women owned construction supply company

Contact Information for Business Card

Name, Title, and phone number and email, web page. maybe spot for qr code.

Font styles to use
Sans Serif

Requirements
Nice to have
• would love to see colors, maybe stylish ribbon dividers or some sort of 2 or 3 tone color card that compliments logo.
Should not have
• Please do not have all white background. Do not include Home/reale state/ or building images.

```html
<!DOCTYPE html>
<html lang="en">
<head>
<meta charset="utf-8">
<title>KX7 Supply – Business Cards</title>
<link rel="stylesheet" href="https://fonts.googleapis.com/css2?family=Montserrat:wght@400;500;700&display=swap">
<style>
  :root {
    --bg: #1c1c1d;
    --paper: #f4f4f3;
    --navy: #1b3a5c;
    --teal: #2596be;
    --white: #ffffff;
    --ghost: rgba(255,255,255,0.06);
  }
  * { margin: 0; padding: 0; box-sizing: border-box; }
  html, body { width: 1200px; height: 1059px; overflow: hidden; }
  body {
    background: var(--bg);
    font-family: "Montserrat", sans-serif;
    position: relative;
  }
  .card {
    position: absolute;
    border-radius: 20px;
    overflow: hidden;
    box-shadow: 0 10px 24px rgba(0,0,0,0.55);
  }
  .card-front { left: 257px; top: 89px; width: 687px; height: 390px; background: var(--paper); }
  .card-back  { left: 254px; top: 547px; width: 693px; height: 393px; background: var(--navy); }

  .wave { position: absolute; inset: 0; width: 100%; height: 100%; }

  .brand {
    position: absolute;
    display: flex;
    align-items: center;
    gap: 10px;
    font-weight: 700;
    white-space: nowrap;
  }
  .brand-dot { border-radius: 50%; flex: none; }
  .card-front .brand { left: 40px; top: 100px; color: var(--navy); font-size: 40px; }
  .card-front .brand-dot { width: 18px; height: 18px; background: var(--teal); }

  .card-back .brand { left: 172px; top: 160px; color: var(--white); font-size: 60px; }
  .card-back .brand-dot { width: 24px; height: 24px; background: var(--teal); }

  .watermark {
    position: absolute;
    left: 10px; top: 40px;
    font-size: 300px;
    font-weight: 700;
    color: var(--ghost);
    line-height: 1;
    letter-spacing: -6px;
  }

  .contact-block {
    position: absolute;
    right: 32px;
    top: 169px;
    text-align: right;
    color: var(--white);
  }
  .person-name { font-size: 21px; font-weight: 700; color: var(--teal); letter-spacing: 0.3px; line-height: 1.1; }
  .person-title { font-size: 14px; font-weight: 400; margin-top: 2px; }
  .address { font-size: 14px; line-height: 20px; margin-top: 20px; }
  .contact-list { list-style: none; margin-top: 18px; }
  .contact-list li {
    display: flex; align-items: center; justify-content: flex-end; gap: 9px;
    font-size: 14px; line-height: 25px;
  }
  .contact-list svg { width: 12px; height: 12px; flex: none; }
</style>
</head>
<body>

  <section class="card card-front" aria-label="Business card front">
    <svg class="wave" viewBox="0 0 1168 663" preserveAspectRatio="none" aria-hidden="true">
      <path fill="var(--navy)" d="M0,632 C250,640 400,560 560,440 C760,290 900,160 1168,175 L1168,663 L0,663 Z"/>
      <path fill="var(--teal)" d="M70,622 C300,612 420,535 560,425 C760,268 900,150 1080,160 C900,168 770,295 585,430 C440,540 300,622 70,622 Z"/>
    </svg>

    <div class="brand"><span class="brand-dot"></span>KX7 Supply</div>

    <div class="contact-block">
      <p class="person-name">DANA WHITLOW</p>
      <p class="person-title">CEO/Founder</p>
      <p class="address">P.O Box 4178 Harbour Road<br>Westvale QC 40211</p>
      <ul class="contact-list">
        <li>555.014.2287
          <svg viewBox="0 0 24 24" aria-hidden="true"><path fill="var(--teal)" d="M6.6 10.8a15 15 0 0 0 6.6 6.6l2.2-2.2c.3-.3.7-.4 1-.2 1.1.4 2.3.6 3.6.6.6 0 1 .4 1 1V20c0 .6-.4 1-1 1A17 17 0 0 1 3 4c0-.6.4-1 1-1h3.5c.6 0 1 .4 1 1 0 1.3.2 2.5.6 3.6.1.3 0 .7-.2 1z"/></svg>
        </li>
        <li>info@kx7supply.com.au
          <svg viewBox="0 0 24 24" aria-hidden="true"><path fill="var(--teal)" d="M2 5h20v14H2z"/><path fill="none" stroke="var(--navy)" stroke-width="2" d="M2 5l10 8 10-8"/></svg>
        </li>
        <li>www.kx7supply.com.au
          <svg viewBox="0 0 24 24" aria-hidden="true"><g fill="none" stroke="var(--teal)" stroke-width="2"><circle cx="12" cy="12" r="10"/><ellipse cx="12" cy="12" rx="4.5" ry="10"/><path d="M2 12h20M4 7h16M4 17h16"/></g></svg>
        </li>
      </ul>
    </div>
  </section>

  <section class="card card-back" aria-label="Business card back">
    <div class="watermark" aria-hidden="true">KX7</div>
    <div class="brand"><span class="brand-dot"></span>KX7 Supply</div>
  </section>

</body>
</html>
```